Poster for homelessness project (2 day deadline)

Amber Lantern Scheme is an initiative in the UK which aims to ensure that people who are new to sleeping on the street are quickly given assistance to take them out of situation they find themselves in.

It began as a London-based project but is now being rolled out nationwide. I am working for a project based in the north of England.

We need some posters which show an image of a place where a rough sleeper may spend the night with some supporting graphic design.

I have three initial images, but I need to be able to easily swap out the images for others. I would appreciate if you could produce three posters for me, each with a different image.

-
Please note:
My client is quite vague about what they want at the moment and the above words may change. I need the selected product to be a layered raw file that I can amend myself with any Adobe CS5.5 (or below) application.

Any typefaces that you choose need to be easily purchasable online.

Please view formatinfo.pdf for formatting guidelines.

Target Market(s)

The general public. It will be placed in public places.

Industry/Entity Type

Graphic Design

Requirements
Must have
• Must contain the words:

"Tonight someone will sleep rough for the first time. Help us make sure they find the Amber Lantern."

"Would you sleep here? Sleeping rough is dangerous. Make sure everyone finds the Amber Lantern."

-
Nice to have
• I'd like this to be quite bleak, grimy and "urban" in feel.

You may recolour/tint the images in any way to enhance this feeling.

```html
<!DOCTYPE html>
<html lang="en">
<head>
<meta charset="utf-8">
<title>Tonight someone will sleep rough for the first time</title>
<link rel="stylesheet" href="https://fonts.googleapis.com/css2?family=Saira+Stencil+One&family=Over+the+Rainbow&family=Kaushan+Script&family=Fjalla+One&display=swap">
<style>
  :root {
    --rust-gold: #9a6421;
    --rust-brown: #5e3310;
    --ember-red: #8c1c0c;
    --deep-shadow: #2a0e05;
    --chalk-white: #fbf4ea;
  }
  html, body {
    margin: 0;
    padding: 0;
    width: 1200px;
    height: 847px;
    overflow: hidden;
    background: var(--deep-shadow);
  }
  .poster {
    position: relative;
    width: 1200px;
    height: 847px;
    overflow: hidden;
    color: var(--chalk-white);
  }
  .poster__scene {
    position: absolute;
    inset: 0;
    background:
      radial-gradient(ellipse 55% 60% at 88% 18%, rgba(150, 28, 10, 0.85), rgba(150, 28, 10, 0) 70%),
      radial-gradient(ellipse 45% 55% at 25% 45%, rgba(196, 140, 60, 0.75), rgba(196, 140, 60, 0) 75%),
      radial-gradient(ellipse 70% 60% at 50% 110%, rgba(30, 10, 4, 0.9), rgba(30, 10, 4, 0) 70%),
      linear-gradient(100deg, var(--rust-gold) 0%, var(--rust-brown) 55%, var(--ember-red) 80%, var(--deep-shadow) 100%);
  }
  .poster__headline {
    position: absolute;
    left: 0;
    right: 0;
    top: 112px;
    margin: 0;
    text-align: center;
    font-family: "Saira Stencil One", sans-serif;
    font-weight: 400;
    font-size: 226px;
    line-height: 1;
    letter-spacing: 6px;
    text-transform: uppercase;
    text-shadow: 0 2px 6px rgba(40, 12, 4, 0.5);
  }
  .poster__subject {
    position: absolute;
    left: 372px;
    width: 430px;
    top: 352px;
    margin: 0;
    text-align: center;
    font-family: "Over the Rainbow", cursive;
    font-size: 104px;
    line-height: 1.1;
    letter-spacing: -2px;
    text-transform: uppercase;
    color: transparent;
    -webkit-text-stroke: 2px var(--chalk-white);
  }
  .poster__statement {
    position: absolute;
    left: 0;
    right: 0;
    top: 470px;
    margin: 0;
    text-align: center;
    font-family: "Kaushan Script", cursive;
    font-size: 56px;
    line-height: 1.4;
    letter-spacing: 2px;
  }
  .poster__statement-emphasis {
    font-size: 84px;
  }
  .poster__call {
    position: absolute;
    left: 0;
    right: 0;
    top: 700px;
    margin: 0;
    text-align: center;
    font-family: "Fjalla One", sans-serif;
    font-size: 38px;
    line-height: 1.2;
  }
  .poster__question {
    position: absolute;
    left: 0;
    right: 0;
    top: 760px;
    margin: 0;
    text-align: center;
    font-family: "Fjalla One", sans-serif;
    font-size: 27px;
    line-height: 1.2;
  }
</style>
</head>
<body>
  <main class="poster">
    <div class="poster__scene" role="img" aria-label="Photograph of a rusted corrugated metal wall beside a worn wooden bench where a rough sleeper might spend the night, tinted in gold, rust and deep red"></div>
    <h1 class="poster__headline">Tonight</h1>
    <p class="poster__subject">Someone</p>
    <p class="poster__statement">will sleep rough for the <span class="poster__statement-emphasis">first</span> time.</p>
    <p class="poster__call">Help us make sure they find the Amber Lantern.</p>
    <p class="poster__question">Would you sleep here? Sleeping rough is dangerous. Make sure everyone finds the Amber Lantern.</p>
  </main>
</body>
</html>
```